Vireon Spool Business Card Design

This is a start up company that has state of the art patented technology for turbo chargers,that can be used on engines, gas or diesel, for any type of automotive,aviation,marine or industrial purpose.
This technology will provide longer life,lower maintenance and better performance and help produce lower emissions with any turbocharged engine.Red would be a predominate color and the design should communicate the latest technology,economy and
Environmental concern.
This product will initially be distributed in the U.S.A. But should move rapidly to global use.
Updates

Thank you for your design submissions, I have increased the budget for this job because my initial order was too low for the quality of work shown, plus I would Like to see some more options. I have a meeting this Sunday with my other partners and would anticipate being able to give you some feedback by the Beginning of next week. Regards.

Thank you for everyone's participation. The deadline is still open until 6/15 and my partners and I have a meeting Scheduled this weekend. At this time we have not ruled anyone out, But will be making a decision during the course of our meeting and wil Decide which direction we will be going in by the beginning of the week. Thanks again, regards, Tom Brandt.

Hello everybody, Sorry for the delay in communication, we have been very busy in putting the start up together. We are still not decided on the design of the business card and have a wide range to choose from. I would anticipated we shall have an answer within the next two weeks. Regards, Tom Brandt.

Target Market(s)

Manufacturers and wholesalers' of OEM and replacement turbochargers

Industry/Entity Type

Industrial

Contact Information for Business Card

We need a logo that should incorporate the " Vireon, a " possibly super imposed over a turbo charger with the fan blades of the turbocharger showing in the center of the "a" .
Name,title,phone number and email address only, no street/mailing address at this time.
The full name of the company is
" Vireon Spool Dynamics LLC "
For the initial card you can use my info.
Thomas Brandt
VP Sales & Marketing
tbrandt@vireonspooldyn.example
555 014 2286

Requirements
Must have
• The Vireon A, the outline of a turbo charger
Nice to have
• Something classy and simple and worldly (global)
Should not have
• No engines,cars,boats,planes

```html
<!DOCTYPE html>
<html lang="en">
<head>
<meta charset="utf-8">
<title>Vireon Spool – Business Card Front</title>
<link rel="stylesheet" href="https://fonts.googleapis.com/css2?family=Orbitron:wght@900&display=swap">
<style>
  :root {
    --page-bg: #ffffff;
    --card-black: #070707;
    --card-glow: #242424;
    --brand-red: #d9202a;
    --red-dark: #6e0f12;
    --red-bright: #ee2229;
    --silver-light: #f4f4f4;
    --silver-mid: #a9a9a9;
    --silver-dark: #6c6c6c;
    --accent-brown: rgba(70, 34, 28, 0.85);
  }
  * { box-sizing: border-box; }
  html, body {
    margin: 0;
    padding: 0;
    width: 1200px;
    height: 536px;
    overflow: hidden;
    background: var(--page-bg);
  }
  .canvas {
    position: relative;
    width: 1200px;
    height: 536px;
    background: var(--page-bg);
  }
  .card {
    position: absolute;
    left: 0;
    top: 0;
    width: 922px;
    height: 533px;
    border-radius: 44px;
    overflow: hidden;
    background:
      radial-gradient(ellipse 52% 60% at 47% 42%, var(--card-glow) 0%, #151515 45%, var(--card-black) 100%);
  }
  .edge-glow {
    position: absolute;
    left: 720px;
    top: 90px;
    width: 340px;
    height: 380px;
    border-radius: 50%;
    background: radial-gradient(ellipse at 60% 55%, var(--accent-brown) 0%, rgba(70, 34, 28, 0.35) 45%, rgba(70, 34, 28, 0) 72%);
  }
  .brand {
    position: absolute;
    left: 196px;
    top: 196px;
    display: flex;
    align-items: center;
    gap: 46px;
  }
  .brand-dot {
    width: 118px;
    height: 118px;
    border-radius: 50%;
    background: var(--brand-red);
    flex: none;
  }
  .brand-name {
    margin: 0;
    font-family: "Orbitron", sans-serif;
    font-weight: 900;
    font-size: 46px;
    line-height: 49px;
    letter-spacing: 3px;
    color: var(--brand-red);
    text-transform: uppercase;
  }
  .brand-name span { display: block; }
  .stripe {
    position: absolute;
    left: 0;
    width: 100%;
  }
  .stripe-silver {
    top: 451px;
    height: 14px;
    background: linear-gradient(90deg, var(--silver-dark) 0%, var(--silver-mid) 15%, var(--silver-light) 50%, var(--silver-mid) 85%, var(--silver-dark) 100%);
  }
  .stripe-red {
    top: 470px;
    height: 14px;
    background: linear-gradient(90deg, var(--red-dark) 0%, #a5181e 20%, var(--red-bright) 45%, #a5181e 80%, var(--red-dark) 100%);
  }
</style>
</head>
<body>
  <main class="canvas">
    <section class="card" aria-label="Vireon Spool business card front">
      <div class="edge-glow" aria-hidden="true"></div>
      <div class="brand">
        <div class="brand-dot" aria-hidden="true"></div>
        <h1 class="brand-name"><span>Vireon</span><span>Spool</span></h1>
      </div>
      <div class="stripe stripe-silver" aria-hidden="true"></div>
      <div class="stripe stripe-red" aria-hidden="true"></div>
    </section>
  </main>
</body>
</html>
```